Broschüre für unsere Firma
Zielgruppe
Wäscherei Kranwitz / Textilservice
Geschäftskunden
Logos etc. In OneDrive/ Dropbox
https://dateiablage-nord.de/f/x7KpQm2Rv9TzLw4NcYh3
Wir wollen gerne eine 4 seitige Broschüre erstellen lassen, um unsere Firma vorzustellen.
Insbesondere der Service
Berufsbekleidung
Hygiene Gardienenwäsche Service
Hotelmietwäsche
Mitbewerb
http://www.wäscherei-gondelsack.de/index.php/ct-menu-item-17/ct-menu-item-25
http://www.waesche-tulpa.ch/download
Im Anhang finden Sie Bilder Logo und Flyers welche wir mal selbst gemacht haben!
Datein sind im OneDrive
Aufgabenstellung

```html
<!DOCTYPE html>
<html lang="de">
<head>
<meta charset="utf-8">
<title>Wäscherei Kranwitz – Broschüre</title>
<link rel="stylesheet" href="https://fonts.googleapis.com/css2?family=Arimo:wght@400;700&family=Tinos&display=swap">
<style>
  :root {
    --stage: #d6d6d6;
    --paper: #f3f1ec;
    --paper-warm: #ebe6de;
    --fabric-light: #fbfaf8;
    --fabric-shade: #cfcac3;
    --ink: #4d4d4d;
    --ink-soft: #5e5e5e;
    --taupe: #b9a998;
    --frame: #c9b9a6;
    --seal-green: #2f8a3e;
  }
  * { box-sizing: border-box; margin: 0; padding: 0; }
  html, body { width: 1200px; height: 2880px; overflow: hidden; }
  body { background: var(--stage); font-family: "Arimo", Arial, sans-serif; color: var(--ink); }

  .row { position: absolute; left: 0; width: 1200px; height: 960px; display: flex; align-items: center; justify-content: center; }
  .row--outside { top: 0; }
  .row--inside { top: 960px; }
  .row--cover { top: 1920px; }

  .spread { display: flex; box-shadow: 0 18px 40px rgba(0,0,0,.18); }
  .panel {
    position: relative; width: 360px; height: 765px; overflow: hidden;
    background: linear-gradient(180deg, var(--paper) 0%, var(--paper-warm) 100%);
  }
  .panel + .panel { border-left: 1px solid rgba(0,0,0,.06); }

  .heading-serif {
    font-family: "Tinos", "Times New Roman", serif; font-weight: 400;
    text-transform: uppercase; letter-spacing: 1px; text-align: center;
    font-size: 17px; color: var(--ink-soft);
  }
  .body-copy { font-size: 12.5px; line-height: 1.72; text-align: center; color: var(--ink); }
  .body-copy p { margin: 0; }

  .divider { position: absolute; height: 3px; background: var(--taupe); border-radius: 2px; }

  .photo {
    position: absolute; border: 5px solid var(--frame);
    box-shadow: 0 3px 8px rgba(0,0,0,.25);
  }
  .fabric { position: absolute; left: 0; width: 100%; }

  /* outside */
  .about .heading-serif { position: absolute; top: 70px; left: 0; width: 100%; }
  .about .body-copy { position: absolute; top: 130px; left: 40px; right: 40px; }
  .about .photo { left: 40px; right: 40px; top: 490px; height: 170px;
    background: radial-gradient(ellipse at 50% 55%, #d9d9d9 0%, #8c8c8c 45%, #3f3f3f 100%); }

  .contact .divider { left: 50px; right: 50px; }
  .contact-block { position: absolute; top: 230px; left: 0; width: 100%; text-align: center; font-size: 12.5px; line-height: 1.8; }
  .contact-block .company { font-weight: 700; font-size: 14px; margin-bottom: 14px; }
  .seals { position: absolute; top: 610px; left: 0; width: 100%; display: flex; justify-content: center; gap: 26px; align-items: center; }
  .seal-square { width: 48px; height: 86px; background: var(--seal-green); }
  .seal-round { width: 64px; height: 64px; border-radius: 50%; background: var(--seal-green); }

  .cover .fabric--top { top: 0; height: 120px;
    background: linear-gradient(180deg, #d8d4ce 0%, var(--fabric-light) 55%, rgba(243,241,236,0) 100%); }
  .cover .fabric--bottom { bottom: 0; height: 300px;
    background: linear-gradient(180deg, rgba(243,241,236,0) 0%, var(--fabric-light) 30%, var(--fabric-shade) 70%, #e4e0da 100%); }
  .brand { position: absolute; top: 185px; left: 0; width: 100%; display: flex; align-items: center; justify-content: center; gap: 12px; }
  .brand-dot { width: 46px; height: 46px; border-radius: 50%; background: #222; }
  .brand-name { font-family: "Arimo", Arial, sans-serif; font-weight: 700; font-size: 25px; color: #222; }
  .claim { position: absolute; top: 360px; left: 0; width: 100%; text-align: center;
    font-weight: 700; font-size: 21px; line-height: 1.75; color: var(--ink-soft); text-transform: uppercase; }

  /* inside */
  .service .photo { left: 50px; right: 50px; top: 40px; height: 145px; }
  .service .heading-serif { position: absolute; top: 215px; left: 20px; right: 20px; line-height: 1.3; }
  .service .body-copy { position: absolute; top: 280px; left: 42px; right: 42px; }
  .service .divider { left: 50px; right: 50px; top: 560px; }
  .service .fabric { bottom: 0; height: 220px;
    background: linear-gradient(180deg, rgba(243,241,236,0) 0%, var(--fabric-light) 45%, #dcd7d0 100%); }
  .photo--workwear { background: linear-gradient(135deg, #d9e4ea 0%, #b8c9d2 50%, #eef1f2 100%); }
  .photo--hygiene { background: linear-gradient(135deg, #6e6e70 0%, #c9c9c9 40%, #b53a3a 60%, #e6e3df 100%); }
  .photo--hotel { background: linear-gradient(135deg, #d3a98b 0%, #f1d9c8 45%, #f7f3ee 100%); }

  .slogan { position: absolute; left: 0; right: 0; top: 655px; text-align: center;
    font-weight: 700; font-size: 25px; color: var(--ink-soft); z-index: 2; }
  .spread--inside { position: relative; }
</style>
</head>
<body>

<section class="row row--outside">
  <div class="spread">
    <article class="panel about">
      <h2 class="heading-serif">Über uns</h2>
      <div class="body-copy">
        <p>Nam ilit illibusant litibus maxim veliquas antis dunte idestio.</p>
        <p>Nectae andissi modigentius quam qui dolorum harchic tionsedi ullatem doluptibus idem fugit reruptas volorem autest, exces et exvenimpos eium autet quas alique voluptatem quisquatis con con nectus, sitas aliquid et dus.</p>
        <p>Ur renimus aligendande moluptassi nis soluptam eatum harchiliti ommos nis et ap qeos ipitem qui ra ium consequia suntur mincidenti nus.</p>
        <p>Bus, oessuntur? Ignimimus apernam quibus, vid ut pratusanimus acium, cones ut laborro ratusci ducs, voluptiatur.</p>
      </div>
      <div class="photo" role="img" aria-label="Foto: Wassertropfen, der auf eine Wasseroberfläche fällt"></div>
    </article>

    <article class="panel contact">
      <div class="divider" style="top:180px"></div>
      <div class="contact-block">
        <p class="company">Wäscherei Kranwitz</p>
        <p>Inh. Jonas Kranwitz</p>
        <p>Lindenhofer Str. 12</p>
        <p>49231 Talberg</p>
        <p>Tel. 04123 55870</p>
        <p>E-mail: info@waescherei-kranwitz.de</p>
        <p>Web: www.waescherei-kranwitz.de</p>
      </div>
      <div class="divider" style="top:480px"></div>
      <div class="seals">
        <div class="seal-square" role="img" aria-label="Zertifikatssiegel"></div>
        <div class="seal-round" role="img" aria-label="Gütesiegel"></div>
      </div>
    </article>

    <article class="panel cover">
      <div class="fabric fabric--top" role="img" aria-label="Foto: weißer, fließender Stoff"></div>
      <div class="brand"><span class="brand-dot"></span><span class="brand-name">Wäscherei Kranwitz</span></div>
      <h1 class="claim">Wo Qualität<br>bestimmend ist</h1>
      <div class="fabric fabric--bottom" role="img" aria-label="Foto: weiße, gefaltete Wäsche"></div>
    </article>
  </div>
</section>

<section class="row row--inside">
  <div class="spread spread--inside">
    <article class="panel service">
      <div class="fabric" role="img" aria-label="Foto: weißer Stoff"></div>
      <div class="photo photo--workwear" role="img" aria-label="Foto: Arzt im weißen Kittel in einer Praxis"></div>
      <h2 class="heading-serif">Berufsbekleidung</h2>
      <div class="body-copy">
        <p>Nam ilit illibusant litibus maxim veliquas antis dunte idestio.</p>
        <p>Nectae andissi modigentius quam qui dolorum harchic tionsedi ullatem doluptibus id, exces et exvenimpos eium autet quas alique voluptatem quisquatis con con nectus, sitas aliquid et dus.</p>
        <p>Ur renimus aligendande moluptassi nis Bus, oessuntur? Ignimimus apernam quibus, vid ut o ratusci ducs, voluptiatur.</p>
      </div>
      <div class="divider"></div>
    </article>

    <article class="panel service">
      <div class="fabric" role="img" aria-label="Foto: weißer Stoff"></div>
      <div class="photo photo--hygiene" role="img" aria-label="Foto: Mitarbeiterin in roter Kleidung an Industriewaschmaschinen"></div>
      <h2 class="heading-serif">Hygiene Gardienen-<br>wäsche Service</h2>
      <div class="body-copy">
        <p>Nam ilit illibusant litibus maxim veliquas antis dunte idestio.</p>
        <p>Nectae andissi modigentius quam qui dolorum harchic tionsedi ullatem doluptibus idemas aliuid et dus.</p>
        <p>quibus, vid ut pratusanimus acium, cones ut laborro ratusci ducs, voluptiatur. Nectae andissi modigentius quam qui dolorum harchic tionsedi ullatem do Nectae andissi modigentius quam qui dolorum harchic tionsedi ullatem do</p>
      </div>
      <div class="divider"></div>
    </article>

    <article class="panel service">
      <div class="fabric" role="img" aria-label="Foto: weißer Stoff"></div>
      <div class="photo photo--hotel" role="img" aria-label="Foto: Zimmermädchen bezieht ein Hotelbett"></div>
      <h2 class="heading-serif">Hotelmietwäsche</h2>
      <div class="body-copy">
        <p>Et exvenimpos eium autet quas alique voluptatem quisquatis con con nectus, sitas aliquid et dus.</p>
        <p>Ur renimus aligendande moluptassi nis soluptam eatum harchiliti ommos nis et ap qeos ipitem qui ra ium consequia suntur mincidenti nus.</p>
        <p>Bus, oessuntur? Ignimimus apernam quibus, vid ut pratusanimus acium, cones ut laborro ratusci ducs, voluptiatur venimpos eium autet quas aliq</p>
      </div>
      <div class="divider"></div>
    </article>

    <p class="slogan">Testen Sie uns und überzeugen Sie sich von unserer Qualität.</p>
  </div>
</section>

<section class="row row--cover">
  <div class="spread">
    <article class="panel cover">
      <div class="fabric fabric--top" role="img" aria-label="Foto: weißer, fließender Stoff"></div>
      <div class="brand"><span class="brand-dot"></span><span class="brand-name">Wäscherei Kranwitz</span></div>
      <h1 class="claim">Wo Qualität<br>bestimmend ist</h1>
      <div class="fabric fabric--bottom" role="img" aria-label="Foto: weiße, gefaltete Wäsche"></div>
    </article>
  </div>
</section>

</body>
</html>
```